Innovative Consulting Firm Needs New Business Cards and Stationary

Our Innovative Consulting Firm, Larkfield Consulting, is in need of new business cards and stationary designs. We want two-sided cards that incorporate our logo, which is attached. We are looking for something not too formal, but is professional and slick.

Card should have the following information:
Name (ex. Tom Bradley)
Title (ex. Manager)
Address (ex. 24680 Cedar Lane)
Address 2 (ex. Suite 100)
City
State
Zip Code
Mobile
Email

The card should also have our website: www.larkfieldconsulting.example

Industry/Entity Type

Management Consulting

Contact Information for Business Card

Name (ex. Tom Bradley)
Title (ex. Manager)
Address 2 (ex. Suite 100)
City
State
Zip Code
Mobile
Email

Font styles to use
Sans Serif

Requirements
Must have
• The colors on the card must match the colors in the logo. The exact color codes are attached in a pdf.
Nice to have
• The Company's Tagline is "Focused on your Future". This might be nice to incorporate, but not necessary.

```html
<!DOCTYPE html>
<html lang="en">
<head>
<meta charset="utf-8">
<title>Larkfield Consulting – Business Card</title>
<link rel="stylesheet" href="https://fonts.googleapis.com/css2?family=Montserrat:wght@400;500;600&family=Exo+2:wght@700&display=swap">
<style>
  :root {
    --brand-blue: #1e4f7b;
    --brand-yellow: #f4ae1a;
    --card-white: #ffffff;
    --backdrop: #e8e9eb;
  }
  * { margin: 0; padding: 0; box-sizing: border-box; }
  html, body { width: 1200px; height: 926px; overflow: hidden; }
  body {
    background: var(--backdrop);
    font-family: "Montserrat", sans-serif;
    position: relative;
  }
  .card {
    position: absolute;
    top: 117px;
    width: 397px;
    height: 694px;
    border-radius: 26px;
    overflow: hidden;
  }
  .card--front { left: 185px; background: var(--card-white); }
  .card--back { left: 619px; background: var(--brand-blue); }

  .wordmark {
    position: absolute;
    font-family: "Montserrat", sans-serif;
    font-weight: 600;
    font-size: 29px;
    letter-spacing: 0.2px;
    white-space: nowrap;
  }
  .card--front .wordmark { top: 84px; left: 0; width: 100%; text-align: center; color: var(--brand-blue); }
  .card--back .wordmark { top: 326px; left: 0; width: 100%; text-align: center; color: var(--card-white); }

  .tagline {
    position: absolute;
    top: 250px;
    left: 0;
    width: 100%;
    height: 26px;
    display: flex;
    align-items: center;
  }
  .tagline__bar { width: 20px; height: 14px; background: var(--brand-yellow); }
  .tagline__tick { width: 4px; height: 14px; background: var(--brand-blue); margin: 0 6px; }
  .tagline__text {
    flex: 1;
    text-align: center;
    font-family: "Exo 2", sans-serif;
    font-weight: 700;
    font-size: 19.5px;
    color: var(--brand-blue);
    letter-spacing: 0.2px;
    white-space: nowrap;
  }
  .tagline__bar--right { margin-left: auto; }

  .wave { position: absolute; left: 0; top: 0; width: 397px; height: 694px; }

  .contact {
    position: absolute;
    left: 0;
    top: 470px;
    width: 100%;
    text-align: center;
    color: var(--card-white);
  }
  .contact__name {
    font-weight: 500;
    font-size: 27px;
    color: var(--brand-yellow);
    letter-spacing: 0.5px;
    line-height: 32px;
  }
  .contact__title { font-size: 16px; line-height: 22px; margin-top: 2px; }
  .contact__icons { display: flex; justify-content: center; gap: 6px; margin: 10px 0 12px; }
  .contact__icons svg { width: 14px; height: 14px; }
  .contact__line { font-size: 17px; line-height: 21.5px; white-space: nowrap; }

  .back-url {
    position: absolute;
    right: 40px;
    top: 626px;
    color: var(--card-white);
    font-size: 17.5px;
    letter-spacing: 0.2px;
  }
</style>
</head>
<body>
  <section class="card card--front">
    <div class="wordmark">Larkfield Consulting</div>

    <div class="tagline">
      <span class="tagline__bar"></span>
      <span class="tagline__tick"></span>
      <span class="tagline__text">FOCUSED ON YOUR FUTURE</span>
      <span class="tagline__tick"></span>
      <span class="tagline__bar tagline__bar--right"></span>
    </div>

    <svg class="wave" viewBox="0 0 397 694" aria-hidden="true">
      <path fill="var(--brand-yellow)" d="M0,475 C90,412 200,385 285,392 C335,396 372,405 397,415 L397,694 L0,694 Z"/>
      <path fill="var(--brand-blue)" d="M0,500 C92,428 200,399 285,402 C335,405 372,413 397,422 L397,694 L0,694 Z"/>
    </svg>

    <div class="contact">
      <div class="contact__name">TOM BRADLEY</div>
      <div class="contact__title">Manager</div>
      <div class="contact__icons" aria-hidden="true">
        <svg viewBox="0 0 14 14"><rect x="3.5" y="1" width="7" height="12" rx="1.3" fill="none" stroke="var(--brand-yellow)" stroke-width="1.4"/><circle cx="7" cy="10.8" r="0.8" fill="var(--brand-yellow)"/></svg>
        <svg viewBox="0 0 14 14"><rect x="1" y="3" width="12" height="8.5" rx="1" fill="none" stroke="var(--brand-yellow)" stroke-width="1.4"/><path d="M1.5,3.5 L7,8 L12.5,3.5" fill="none" stroke="var(--brand-yellow)" stroke-width="1.4"/></svg>
        <svg viewBox="0 0 14 14"><g fill="none" stroke="var(--brand-yellow)" stroke-width="1.1"><circle cx="7" cy="7" r="5.8"/><ellipse cx="7" cy="7" rx="2.5" ry="5.8"/><path d="M1.2,7 H12.8 M2,4 H12 M2,10 H12"/></g></svg>
        <svg viewBox="0 0 14 14"><path d="M7,13 C4,9 3,7.3 3,5.2 A4,4 0 0 1 11,5.2 C11,7.3 10,9 7,13 Z" fill="var(--brand-yellow)"/><circle cx="7" cy="5.2" r="1.5" fill="var(--brand-blue)"/></svg>
      </div>
      <div class="contact__line">+330 5550-1842</div>
      <div class="contact__line">info@larkfieldconsulting.example</div>
      <div class="contact__line">www.larkfieldconsulting.example</div>
      <div class="contact__line">24680 Cedar Lane Suite 100</div>
    </div>
  </section>

  <section class="card card--back">
    <div class="wordmark">Larkfield Consulting</div>
    <div class="back-url">www.larkfieldconsulting.example</div>
  </section>
</body>
</html>
```